Varden Hub, LLC. is the name of the company that will be an Internet startup working in E-commerce and

We are a new company and going to start the business by hiring people we need. We are on “Hiring Now…” status right now which we like to be displayed on the website homepage.
The website should allow us to start the hiring process with letting people see and apply for jobs posted on the website.

the company logo is attached.

Target Market(s)

Tech Job Seekers, Programmers, iOS and Android Developers, Software engineers, Graphic designers, QA engineers, Customer Service Reps,...

Industry/Entity Type

Internet

Number of Pages Required

5+ page

Font styles to use
Serif
Sans Serif

Colors

Designer to choose colors to be used in the design.

Requirements
Must have
• We need a system to help job seekers to upload the resume and cover letter and fill the required forms and answer some questions on a form designed to evaluate the job seekers and let them know if they fit in the position and should apply for it.
• We also want job seekers to do a Pre-Employment Tests including Aptitude, Personality, and Skills after they qualified for a job which links our website to web-based pre-employment testing services websites like (Metrica, Talvex, Brunholt & Partners, Dovin Evaluation, …)

```html
<!DOCTYPE html>
<html lang="en">
<head>
<meta charset="utf-8">
<title>Varden Hub – Hiring Now</title>
<link href="https://fonts.googleapis.com/css2?family=Open+Sans:wght@400;600;700;800&display=swap" rel="stylesheet">
<style>
:root{
  --orange:#ff4e0b;
  --blue:#2f8ac3;
  --teal:#67c4cf;
  --navy:#2f7fb8;
  --ink:#333;
  --grey-bg:#efefef;
  --footer:#3b3b3c;
  --line:#dcdcdc;
  --white:#fff;
}
*{box-sizing:border-box;margin:0;padding:0}
html,body{width:738px;height:1200px;overflow:hidden}
body{font-family:"Open Sans",Arial,sans-serif;color:var(--ink);background:var(--white);position:relative}

/* hero */
.hero{position:absolute;left:0;top:0;width:738px;height:428px}
.hero-photo{position:absolute;inset:0;background:linear-gradient(180deg,#ece8e3 0%,#e2ddd6 45%,#8c8a8c 75%,#3d4350 100%)}
.brand{position:absolute;left:82px;top:17px;display:flex;align-items:center;gap:5px;font-weight:800;font-size:18px;color:var(--blue);letter-spacing:-.4px;white-space:nowrap}
.brand-dot{width:8px;height:8px;background:var(--orange)}
.nav{position:absolute;top:12px;left:485px;display:flex;font-size:7px;text-transform:uppercase}
.nav a{color:#222;text-decoration:none;padding:0 7px;line-height:13px;display:block}
.nav a.active{background:var(--blue);color:var(--white);font-weight:700}
.hiring{position:absolute;top:64px;width:100%;text-align:center;font-size:18px;font-weight:600;color:#111}
.field{position:absolute;top:110px;height:27px;width:143px;background:var(--white);box-shadow:0 2px 4px rgba(0,0,0,.25);font-size:6.5px;display:flex;align-items:center;padding-left:7px;gap:6px;color:#222}
.field .upload{position:absolute;right:6px;top:7px;background:var(--blue);color:var(--white);font-weight:700;font-size:6.5px;padding:2px 4px}
.btn{position:absolute;background:var(--orange);color:var(--white);font-weight:800;text-transform:uppercase;text-align:center;white-space:nowrap}
.btn-apply{left:310px;top:163px;width:118px;height:29px;line-height:29px;font-size:10px;box-shadow:0 3px 5px rgba(0,0,0,.3)}
.btn-tests{left:273px;top:394px;width:192px;height:34px;line-height:31px;font-size:9px;border:2px solid var(--teal);border-bottom:none}

/* intro band */
.intro{position:absolute;top:428px;left:0;width:738px;height:229px;background:var(--teal)}
.intro svg.band{position:absolute;left:0;top:0}
.intro h2{position:absolute;font-size:11.5px;font-weight:700;color:var(--white);text-transform:uppercase}
.rule{position:absolute;height:2px;background:var(--blue)}
.intro p{position:absolute;left:82px;width:246px;font-size:6.8px;line-height:12px;color:#2d4f56}
.jobs{position:absolute;left:434px;top:65px;width:216px}
.job{height:44px;border-bottom:1px solid rgba(255,255,255,.18);position:relative;color:var(--white);font-size:7px;padding:8px 0 0 28px;line-height:12px}
.job small{font-size:5px;text-transform:uppercase}
.job svg{position:absolute;left:8px;top:14px}
.btn-small{height:18px;line-height:18px;font-size:7px}

/* browse */
.sec-title{position:absolute;width:100%;text-align:center;font-size:11.5px;font-weight:700;color:var(--navy);text-transform:uppercase}
.sec-rule{position:absolute;left:349px;width:40px;height:2px;background:var(--orange)}
.browse{position:absolute;left:99px;top:758px;width:540px;height:184px;border:1px solid var(--line)}
.tabs{position:absolute;top:0;left:0;width:100%;height:24px;border-bottom:1px solid var(--line);font-size:7px}
.tab{position:absolute;top:0;height:23px;line-height:23px;text-align:center;color:#333;white-space:nowrap}
.tab.active{background:var(--orange);color:var(--white)}
.tab-sep{position:absolute;top:6px;width:1px;height:11px;background:var(--line)}
.sector-col{position:absolute;top:47px;list-style:none;font-size:6.8px;color:#444;line-height:14.7px;white-space:nowrap}
.btn-all{left:321px;top:970px;width:96px;height:19px;line-height:19px;font-size:7px}

/* employers */
.employers{position:absolute;top:1025px;left:0;width:738px;height:140px;background:var(--grey-bg)}
.emp{position:absolute;top:90px;width:100px;text-align:center;font-size:6.5px;font-weight:700;color:#666;text-transform:uppercase;line-height:9px}
.emp-sep{position:absolute;top:76px;width:1px;height:36px;background:#ddd}

/* footer */
.footer{position:absolute;top:1165px;left:0;width:738px;height:35px;background:var(--footer);color:var(--white)}
.footer .brand{top:11px;font-size:11px;gap:4px;letter-spacing:-.3px}
.footer .brand-dot{width:5px;height:5px}
.foot-nav{position:absolute;left:158px;top:13px;font-size:5.8px;text-transform:uppercase;white-space:nowrap}
.copy{position:absolute;right:83px;top:13px;font-size:5.8px;white-space:nowrap}
</style>
</head>
<body>

<header class="hero">
  <div class="hero-photo" role="img" aria-label="Photo of five job candidates in business suits waiting on a bench in front of a white brick wall"></div>
  <div class="brand">Varden Hub<span class="brand-dot"></span></div>
  <nav class="nav">
    <a class="active" href="#">Home</a><a href="#">About us</a><a href="#">Jobs</a><a href="#">Contact us</a>
  </nav>
  <h1 class="hiring">Hiring Now...</h1>

  <div class="field" style="left:152px">
    <svg width="8" height="6" viewBox="0 0 8 6"><rect width="8" height="6" fill="#444"/><path d="M0 0l4 3 4-3" stroke="#fff" stroke-width=".8" fill="none"/></svg>E mail
  </div>
  <div class="field" style="left:303px">
    <svg width="7" height="7" viewBox="0 0 7 7"><path d="M3.5 0l3 3H4.5v2h-2V3H.5z M0 6h7v1H0z" fill="#444"/></svg>Upload the resume<span class="upload">UPLOAD</span>
  </div>
  <div class="field" style="left:455px">
    <svg width="7" height="7" viewBox="0 0 7 7"><path d="M3.5 0l3 3H4.5v2h-2V3H.5z M0 6h7v1H0z" fill="#444"/></svg>Upload cover letter<span class="upload">UPLOAD</span>
  </div>
  <a class="btn btn-apply">Apply for jobs</a>
  <a class="btn btn-tests">Pre-employment tests</a>
</header>

<section class="intro">
  <svg class="band" width="738" height="229"><polygon points="367,0 738,0 738,229 395,229" fill="#2f8ac3"/></svg>
  <h2 style="left:82px;top:25px">Welcome to our site</h2>
  <div class="rule" style="left:82px;top:48px;width:58px"></div>
  <p style="top:68px">If you are going to use a passage of Lorem Ipsum, you need to be sure there isn't anything embarrassing hidden in the middle of text</p>
  <p style="top:103px">There are many variations of passages of Lorem Ipsum available, but the majority have suffered alteration in some form, by injected humour, or randomised words which don't look even slightly believable. If you are going to use a passage of Lorem Ipsum, you need to be sure there isn't anything embarrassing hidden in the middle of text</p>
  <a class="btn btn-small" style="left:82px;top:187px;width:65px;height:21px;line-height:21px">Read more</a>

  <h2 style="left:428px;top:25px">Latest job post</h2>
  <div class="rule" style="left:430px;top:48px;width:40px;background:#fff"></div>
  <div class="jobs">
    <div class="job"><svg width="5" height="7"><path d="M1 1l3 2.5L1 6" stroke="#fff" stroke-width="1.4" fill="none"/></svg><small>Job title :</small> Lorem Ipsum is simply dummy text<br><small>Eligibility :</small> Bachelor’s Degree</div>
    <div class="job"><svg width="5" height="7"><path d="M1 1l3 2.5L1 6" stroke="#fff" stroke-width="1.4" fill="none"/></svg><small>Job title :</small> Lorem Ipsum is simply dummy text<br><small>Eligibility :</small> Bachelor’s Degree</div>
    <div class="job" style="border:none"><svg width="5" height="7"><path d="M1 1l3 2.5L1 6" stroke="#fff" stroke-width="1.4" fill="none"/></svg><small>Job title :</small> Lorem Ipsum is simply dummy text<br><small>Eligibility :</small> Bachelor’s Degree</div>
  </div>
  <a class="btn btn-small" style="left:441px;top:196px;width:77px">View all jobs</a>
</section>

<h2 class="sec-title" style="top:692px">Browse for jobs by</h2>
<div class="sec-rule" style="top:720px"></div>

<section class="browse">
  <div class="tabs">
    <span class="tab active" style="left:108px;width:42px">Sector</span>
    <span class="tab" style="left:166px;width:58px">Location</span>
    <span class="tab-sep" style="left:230px"></span>
    <span class="tab" style="left:239px;width:58px">Part time</span>
    <span class="tab-sep" style="left:305px"></span>
    <span class="tab" style="left:311px;width:58px">Full time</span>
    <span class="tab-sep" style="left:373px"></span>
    <span class="tab" style="left:381px;width:58px">Graduate</span>
  </div>
  <ul class="sector-col" style="left:23px">
    <li>Administration 538</li><li>Arts &amp; heritage 336</li><li>Charities 1721</li><li>Construction 88</li><li>Design 262</li><li>Engineering 124</li><li>Environment 114</li><li>Finance &amp; accounting 933</li>
  </ul>
  <ul class="sector-col" style="left:170px">
    <li>Further education 277</li><li>General 431</li><li>Government &amp; politics 545</li><li>Health 739</li><li>Higher education 453</li><li>Hospitality 78</li><li>Housing 375</li><li>Legal 132</li>
  </ul>
  <ul class="sector-col" style="left:316px">
    <li>Leisure 67</li><li>Marketing &amp; PR 1863</li><li>Media 1336</li><li>Recruitment 564</li><li>Retail &amp; FMCG 197</li><li>Sales 706</li><li>Schools 2287</li><li>Science 118</li>
  </ul>
  <ul class="sector-col" style="left:437px">
    <li>Secretarial 67</li><li>Senior executive 480</li><li>Skilled trade 13</li><li>Social care 1063</li><li>Social enterprise 25</li><li>Technology 742</li><li>Travel &amp; transport 146</li>
  </ul>
</section>
<a class="btn btn-all">View all 5,253 jobs</a>

<section class="employers">
  <h2 class="sec-title" style="top:21px">Featured employers</h2>
  <div class="sec-rule" style="top:46px"></div>
  <span class="emp" style="left:68px">Northwind Lung Trust</span>
  <span class="emp-sep" style="left:168px"></span>
  <span class="emp" style="left:168px">Pacora Energy</span>
  <span class="emp-sep" style="left:268px"></span>
  <span class="emp" style="left:267px">Calvert Motors</span>
  <span class="emp-sep" style="left:367px"></span>
  <span class="emp" style="left:367px">Fenwick Medical</span>
  <span class="emp-sep" style="left:467px"></span>
  <span class="emp" style="left:467px">Ramsey Trucks</span>
  <span class="emp-sep" style="left:567px"></span>
  <span class="emp" style="left:570px">Quorvia Systems</span>
</section>

<footer class="footer">
  <div class="brand">Varden Hub<span class="brand-dot"></span></div>
  <div class="foot-nav">Home &nbsp;|&nbsp; About us &nbsp;|&nbsp; Jobs &nbsp;|&nbsp; Contact us</div>
  <div class="copy">Copyrights @ 2017 All Rights Reserved</div>
</footer>

</body>
</html>
```